RWM Bricklaying business card

i need a business card designed for my bricklaying company.
I was also hoping to get a logo drawn up so i can put it on some t-shirts.
You can use any style or colours just as long as it lloks good. thanks Dallas

Dallas Whitby
RWM Bricklaying
0471395067
Any type of brick/blockwork
No job too small

```html
<!DOCTYPE html>
<html lang="en">
<head>
<meta charset="utf-8">
<title>RWM Bricklaying – Business Card</title>
<link rel="stylesheet" href="https://fonts.googleapis.com/css2?family=Open+Sans:wght@400&family=Kalam:wght@300&display=swap">
<style>
  :root {
    --brand-blue: #0e74bb;
    --paper: #ffffff;
    --ink: #3a3a3a;
    --card-edge: #cfcfcf;
    --note-ink: #1e1e1e;
    --uniform-navy: #2f3a6e;
    --uniform-light: #e9e6e3;
  }
  html, body {
    margin: 0;
    padding: 0;
    width: 1200px;
    height: 2218px;
    overflow: hidden;
    background: var(--paper);
  }
  .canvas {
    position: relative;
    width: 1200px;
    height: 2218px;
    font-family: "Open Sans", Arial, sans-serif;
  }
  .card {
    position: absolute;
    left: 108px;
    width: 991px;
    box-sizing: border-box;
  }
  .card--front {
    top: 108px;
    height: 552px;
    border: 2px solid var(--card-edge);
    background: var(--paper);
  }
  .brand {
    position: absolute;
    right: 30px;
    top: 40px;
    display: flex;
    align-items: center;
    gap: 18px;
    color: var(--ink);
  }
  .brand__square {
    width: 70px;
    height: 70px;
    background: var(--brand-blue);
  }
  .brand__name {
    display: flex;
    flex-direction: column;
    align-items: flex-end;
    font-weight: 400;
    line-height: 1;
  }
  .brand__initials {
    font-size: 62px;
    letter-spacing: 2px;
  }
  .brand__trade {
    margin-top: 8px;
    font-size: 22px;
    letter-spacing: 5px;
  }
  .front-band {
    position: absolute;
    left: 29px;
    top: 209px;
    width: 929px;
    height: 310px;
    background: var(--brand-blue);
    color: var(--paper);
  }
  .front-band__name {
    position: absolute;
    left: 38px;
    top: 38px;
    margin: 0;
    font-size: 38px;
    font-weight: 400;
  }
  .front-band__phone {
    position: absolute;
    left: 38px;
    top: 90px;
    margin: 0;
    font-size: 29px;
    letter-spacing: 1px;
  }
  .front-band__tagline {
    position: absolute;
    left: 38px;
    bottom: 20px;
    margin: 0;
    font-size: 27px;
    letter-spacing: 4.4px;
  }
  .card--back {
    top: 735px;
    height: 547px;
    background: var(--brand-blue);
  }
  .appointment {
    position: absolute;
    left: 31px;
    top: 208px;
    width: 929px;
    height: 310px;
    background: var(--paper);
  }
  .appointment__note {
    position: absolute;
    margin: 0;
    font-family: "Kalam", "Comic Sans MS", cursive;
    font-weight: 300;
    font-size: 42px;
    color: var(--note-ink);
    transform: rotate(-4deg) skewX(-8deg);
    transform-origin: left bottom;
    white-space: nowrap;
    line-height: 1;
  }
  .appointment__note--heading { left: 131px; top: 60px; }
  .appointment__note--date { left: 109px; top: 112px; }
  .appointment__note--cost { left: 97px; top: 204px; }
  .uniform-photo {
    position: absolute;
    left: 326px;
    top: 1330px;
    width: 600px;
    height: 888px;
    background: linear-gradient(180deg, var(--uniform-light) 0%, var(--uniform-light) 14%, var(--uniform-navy) 26%, var(--uniform-navy) 100%);
  }
</style>
</head>
<body>
<main class="canvas">
  <section class="card card--front" aria-label="Business card front">
    <div class="brand">
      <span class="brand__square"></span>
      <div class="brand__name">
        <span class="brand__initials">RWM</span>
        <span class="brand__trade">BRICKLAYING</span>
      </div>
    </div>
    <div class="front-band">
      <h1 class="front-band__name">Dallas Whitby</h1>
      <p class="front-band__phone">0471 395 067</p>
      <p class="front-band__tagline">Any type of brick/blockwork No job too small</p>
    </div>
  </section>

  <section class="card card--back" aria-label="Business card back">
    <div class="appointment">
      <p class="appointment__note appointment__note--heading">Next appointment</p>
      <p class="appointment__note appointment__note--date">January 21 at 10.30am</p>
      <p class="appointment__note appointment__note--cost">cost is $2000</p>
    </div>
  </section>

  <div class="uniform-photo" role="img" aria-label="Photo of a tradesman in navy work overalls with a tool belt, wearing the RWM Bricklaying logo on the chest"></div>
</main>
</body>
</html>
```